Make an Awesome Graphic for a PPT

Attached is the specific content for the project. the X-factor of Adoption. It does not need a title just take the existing graphic an improve it. Attached is our company logo for color palette and the "ugly version". It should look modern and edge in terms of effect and font. Need it by Monday March 7th

```html
<!DOCTYPE html>
<html lang="en">
<head>
<meta charset="utf-8">
<title>The X-Factor of Adoption</title>
<link rel="stylesheet" href="https://fonts.googleapis.com/css2?family=Open+Sans:wght@300;400;700;800&display=swap">
<style>
  :root {
    --bg: #ffffff;
    --arm-experience: #7b5c44;
    --arm-concept-top: #0f98b6;
    --arm-concept-bottom: #a3c13f;
    --arm-sentiment: #0b5fae;
    --hub: #ffffff;
    --hub-text: #1a4f9e;
    --label: #ffffff;
  }
  html, body {
    margin: 0;
    padding: 0;
    width: 1200px;
    height: 1200px;
    overflow: hidden;
    background: var(--bg);
  }
  .adoption-diagram {
    display: block;
    width: 1200px;
    height: 1200px;
  }
  .arm { stroke-width: 12; stroke-linejoin: round; }
  .arm--experience { fill: var(--arm-experience); stroke: var(--arm-experience); }
  .arm--concept-top { fill: var(--arm-concept-top); stroke: var(--arm-concept-top); }
  .arm--concept-bottom { fill: var(--arm-concept-bottom); stroke: var(--arm-concept-bottom); }
  .arm--sentiment { fill: var(--arm-sentiment); stroke: var(--arm-sentiment); }
  .arm-label {
    font-family: "Open Sans", sans-serif;
    font-weight: 300;
    font-size: 11.5px;
    fill: var(--label);
  }
  .bulb-icon {
    fill: none;
    stroke: var(--label);
    stroke-width: 2.2;
    stroke-linecap: round;
    stroke-linejoin: round;
  }
  .icon-slot { fill: var(--label); opacity: 0.9; }
  .hub-circle { fill: var(--hub); }
  .hub-title {
    font-family: "Open Sans", sans-serif;
    font-weight: 800;
    font-size: 15px;
    fill: var(--hub-text);
    text-anchor: middle;
    letter-spacing: 0.2px;
  }
  .hub-icon-slot { fill: var(--hub-text); }
</style>
</head>
<body>
<svg class="adoption-diagram" viewBox="0 0 500 500" xmlns="http://www.w3.org/2000/svg">
  <defs>
    <filter id="hub-shadow" x="-30%" y="-30%" width="160%" height="160%">
      <feDropShadow dx="0" dy="2" stdDeviation="4" flood-color="#000" flood-opacity="0.28"/>
    </filter>
  </defs>

  <g class="arms">
    <polygon class="arm arm--experience" points="96,52 198,48 306,244 202,244"/>
    <polygon class="arm arm--concept-top" points="302,48 410,52 300,244 196,244"/>
    <polygon class="arm arm--concept-bottom" points="196,244 300,244 198,434 96,438"/>
    <polygon class="arm arm--sentiment" points="202,244 306,244 410,438 302,434"/>
  </g>

  <g class="segment segment--experience">
    <text class="arm-label" x="124" y="90">Farmer</text>
    <text class="arm-label" x="134" y="106">Experience</text>
    <circle class="icon-slot" cx="184" cy="142" r="14" role="img" aria-label="Head with gear icon for farmer experience"/>
  </g>

  <g class="segment segment--concept-top">
    <text class="arm-label" x="325" y="90">Innovation</text>
    <text class="arm-label" x="315" y="106">Concept</text>
    <g class="bulb-icon" transform="translate(318,142)">
      <path d="M-7,6 C-12,2 -11,-10 0,-11 C11,-10 12,2 7,6 L6,10 L-6,10 Z"/>
      <line x1="-5" y1="14" x2="5" y2="14"/>
      <path d="M-4,4 L0,-2 L4,4"/>
      <line x1="0" y1="-17" x2="0" y2="-21"/>
      <line x1="-13" y1="-11" x2="-16" y2="-14"/>
      <line x1="13" y1="-11" x2="16" y2="-14"/>
      <line x1="-17" y1="0" x2="-21" y2="0"/>
      <line x1="17" y1="0" x2="21" y2="0"/>
    </g>
  </g>

  <g class="segment segment--concept-bottom">
    <g class="bulb-icon" transform="translate(190,328)">
      <path d="M-7,6 C-12,2 -11,-10 0,-11 C11,-10 12,2 7,6 L6,10 L-6,10 Z"/>
      <line x1="-5" y1="14" x2="5" y2="14"/>
      <path d="M-4,4 L0,-2 L4,4"/>
      <line x1="0" y1="-17" x2="0" y2="-21"/>
      <line x1="-13" y1="-11" x2="-16" y2="-14"/>
      <line x1="13" y1="-11" x2="16" y2="-14"/>
      <line x1="-17" y1="0" x2="-21" y2="0"/>
      <line x1="17" y1="0" x2="21" y2="0"/>
    </g>
    <text class="arm-label" x="145" y="377">Innovation</text>
    <text class="arm-label" x="136" y="393">Concept</text>
  </g>

  <g class="segment segment--sentiment">
    <ellipse class="icon-slot" cx="312" cy="330" rx="19" ry="14" role="img" aria-label="Sentiment icon showing happy and sad expressions"/>
    <text class="arm-label" x="312" y="384">Farmer</text>
    <text class="arm-label" x="320" y="400">Sentiment</text>
  </g>

  <g class="hub">
    <circle class="hub-circle" cx="251" cy="245" r="60" filter="url(#hub-shadow)"/>
    <rect class="hub-icon-slot" x="241" y="197" width="20" height="26" rx="6" role="img" aria-label="Hand icon for adoption"/>
    <text class="hub-title" x="251" y="252">ADOPTION</text>
    <text class="hub-title" x="251" y="272">ZONE</text>
  </g>
</svg>
</body>
</html>
```